International Medical travel company needs professional card

We just purchased a logo through sketch nest, and now need a business card. We contract with Middle Eastern governments to bring patients who need complex medical care to the U.S. for treatment. We will upload logo. Titles, names, contact info, etc. needs to be in English on one side, Arabic on the other

Target Market(s)

Health administrators, professionals

Industry/Entity Type

Health Care

Contact Information for Business Card

logo on each side. Usual name/title/contact info

Font styles to use
Serif
Sans Serif

Colors
0255a3

Requirements
Must have
• English one side, Arabic the other

```html
<!DOCTYPE html>
<html lang="en">
<head>
<meta charset="utf-8">
<title>Halcyon Health – Business Card</title>
<link href="https://fonts.googleapis.com/css2?family=Source+Sans+3:wght@400;600&family=Noto+Naskh+Arabic:wght@400;600&display=swap" rel="stylesheet">
<style>
  :root {
    --backdrop-top: #2a2a2a;
    --backdrop-bottom: #050505;
    --card-white: #f3f3f3;
    --olive: #8a8414;
    --gold-light: #e2dc62;
    --gold-mid: #b7ae2a;
    --gold-dark: #8c8410;
    --brand-blue: #0255a3;
    --ink: #2e2e2e;
    --white: #ffffff;
  }
  html, body {
    margin: 0;
    padding: 0;
    width: 1200px;
    height: 900px;
    overflow: hidden;
  }
  body {
    position: relative;
    background: radial-gradient(ellipse at 50% 0%, var(--backdrop-top) 0%, #161616 55%, var(--backdrop-bottom) 100%);
    font-family: "Source Sans 3", "Myriad Pro", sans-serif;
  }
  .card {
    position: absolute;
    top: 184px;
    height: 491px;
    border-radius: 14px;
    box-sizing: border-box;
    text-align: center;
  }
  .card--front {
    left: 299px;
    width: 301px;
    background: var(--card-white);
    color: var(--ink);
  }
  .card--back {
    left: 645px;
    width: 305px;
    background: radial-gradient(circle at 45% 48%, var(--gold-light) 0%, var(--gold-mid) 45%, var(--gold-dark) 85%);
    color: var(--white);
  }
  .brand-square {
    position: absolute;
    left: 103px;
    top: 34px;
    width: 94px;
    height: 94px;
    border: 4px solid var(--olive);
    box-sizing: border-box;
  }
  .brand-name {
    position: absolute;
    left: 0;
    right: 0;
    margin: 0;
    font-weight: 400;
    letter-spacing: 1px;
    line-height: 1;
    white-space: nowrap;
  }
  .card--front .brand-name {
    top: 160px;
    font-size: 34px;
    color: var(--olive);
  }
  .card--back .brand-name {
    top: 398px;
    font-size: 36px;
    color: var(--white);
  }
  .person {
    position: absolute;
    top: 268px;
    left: 0;
    right: 0;
  }
  .person__name {
    margin: 0;
    font-size: 20px;
    font-weight: 600;
    line-height: 1.1;
  }
  .person__first { color: var(--olive); }
  .person__last { color: var(--brand-blue); }
  .person__title {
    margin: 2px 0 0;
    font-size: 15px;
  }
  .contact {
    position: absolute;
    top: 342px;
    left: 0;
    right: 0;
    font-size: 15px;
    line-height: 20px;
  }
  .contact__row {
    display: flex;
    justify-content: center;
    align-items: center;
    gap: 8px;
  }
  .contact__icon { width: 11px; height: 9px; fill: var(--olive); }
  .address {
    position: absolute;
    top: 420px;
    left: 0;
    right: 0;
    margin: 0;
    font-size: 15px;
    line-height: 16px;
    font-style: normal;
  }
  .arabic-details {
    position: absolute;
    top: 120px;
    left: 20px;
    right: 20px;
    font-family: "Noto Naskh Arabic", serif;
    color: var(--white);
    text-shadow: 0 1px 2px rgba(0, 0, 0, 0.25);
  }
  .arabic-details__name {
    margin: 0;
    font-size: 22px;
    font-weight: 600;
    line-height: 1.3;
  }
  .arabic-details__title {
    margin: 0 0 18px;
    font-size: 16px;
    line-height: 1.4;
  }
  .arabic-details__line {
    margin: 0;
    font-size: 15px;
    line-height: 1.6;
  }
  .arabic-details__line--latin {
    font-family: "Source Sans 3", sans-serif;
    direction: ltr;
  }
  .arabic-details__address {
    margin: 16px 0 0;
    font-size: 15px;
    line-height: 1.5;
    font-style: normal;
  }
</style>
</head>
<body>
  <section class="card card--front">
    <div class="brand-square"></div>
    <p class="brand-name">HALCYON HEALTH</p>

    <div class="person">
      <p class="person__name"><span class="person__first">JOHN</span> <span class="person__last">SMITH</span></p>
      <p class="person__title">Managing Direcator</p>
    </div>

    <div class="contact">
      <div class="contact__row">
        <svg class="contact__icon" viewBox="0 0 11 9" aria-hidden="true">
          <path d="M0 3 Q5.5 -1 11 3 L9 4 L8 2.6 L3 2.6 L2 4 Z"/>
          <rect x="2" y="4" width="7" height="5" rx="1"/>
        </svg>
        <span>823-456-7890</span>
      </div>
      <div class="contact__row">
        <svg class="contact__icon" viewBox="0 0 11 9" aria-hidden="true">
          <rect x="0" y="1" width="11" height="8"/>
          <path d="M0 1 L5.5 5 L11 1" fill="none" stroke="#f3f3f3" stroke-width="1"/>
        </svg>
        <span>info@youremail.com</span>
      </div>
    </div>

    <address class="address">1234, Address Goes Here<br>Country Name, 123456</address>
  </section>

  <section class="card card--back">
    <div class="arabic-details" lang="ar" dir="rtl">
      <p class="arabic-details__name">جون سميث</p>
      <p class="arabic-details__title">المدير العام</p>
      <p class="arabic-details__line arabic-details__line--latin">823-456-7890</p>
      <p class="arabic-details__line arabic-details__line--latin">info@youremail.com</p>
      <address class="arabic-details__address">١٢٣٤، العنوان هنا<br>اسم الدولة، ١٢٣٤٥٦</address>
    </div>
    <p class="brand-name">HALCYON HEALTH</p>
  </section>
</body>
</html>
```